Poster Design

Hello,

My name is Rowan Pickett and I run a vidora channel called 'CrumbleDiary'. I want a poster made for those who watch my video to purchase and put on their wall at home. The poster will be all text and as you can see, I've attached a few examples of posters which I would like it to be similar to. I use a lot of the colour #ab6f7f so it would be good to incorporate this in somewhere (maybe the background colour).
I would like the poster to say:
"Do More Of What Makes YOU Happy"
I need this poster to be for sale ready for christmas, so Im going to need the designs created as soon as possible. Im sorry for the rush.
Have fun with it and feel free to upload multiple versions of a design as well as a few designs if you like.
I look forward to seeing what you come up with.
Rowan
(Of course I will need to own all rights once the payment has been made)

```html
<!DOCTYPE html>
<html lang="en">
<head>
<meta charset="UTF-8">
<title>Do More Of What Makes You Happy – Poster</title>
<link rel="stylesheet" href="https://fonts.googleapis.com/css2?family=Courier+Prime&family=Kalam:wght@400&display=swap">
<style>
  :root {
    --ink-white: #ffffff;
    --ink-edge: rgba(120, 40, 70, 0.55);
    --pink-hot: #f0529e;
    --pink-magenta: #e5207a;
    --pink-soft: #f47fb6;
    --red-bright: #e41f3f;
    --red-deep: #8c0a22;
    --peach: #f26a7a;
  }
  html, body {
    margin: 0;
    padding: 0;
    width: 848px;
    height: 1200px;
    overflow: hidden;
  }
  .poster {
    position: relative;
    width: 848px;
    height: 1200px;
    overflow: hidden;
  }
  .poster__paint {
    position: absolute;
    inset: 0;
    background:
      radial-gradient(ellipse 300px 160px at 760px 420px, var(--red-bright) 0%, rgba(228,31,63,0) 100%),
      radial-gradient(ellipse 220px 120px at 560px 640px, rgba(228,31,63,0.7) 0%, rgba(228,31,63,0) 100%),
      radial-gradient(ellipse 420px 380px at 820px 1160px, var(--red-deep) 0%, rgba(140,10,34,0) 100%),
      radial-gradient(ellipse 300px 220px at 380px 1120px, rgba(200,20,50,0.8) 0%, rgba(200,20,50,0) 100%),
      radial-gradient(ellipse 360px 260px at 120px 120px, var(--pink-magenta) 0%, rgba(229,32,122,0) 100%),
      radial-gradient(ellipse 300px 140px at 200px 500px, rgba(247,150,170,0.8) 0%, rgba(247,150,170,0) 100%),
      radial-gradient(ellipse 260px 120px at 420px 380px, var(--pink-soft) 0%, rgba(244,127,182,0) 100%),
      radial-gradient(ellipse 400px 200px at 160px 900px, var(--pink-hot) 0%, rgba(240,82,158,0) 100%),
      radial-gradient(ellipse 320px 160px at 640px 80px, var(--pink-soft) 0%, rgba(244,127,182,0) 100%),
      linear-gradient(160deg, var(--pink-hot) 0%, var(--pink-magenta) 55%, #d0183e 100%);
  }
  .poster__grain {
    position: absolute;
    inset: 0;
    width: 848px;
    height: 1200px;
    opacity: 0.22;
    mix-blend-mode: soft-light;
  }
  .poster__text {
    position: absolute;
    left: 0;
    width: 100%;
    text-align: center;
    color: var(--ink-white);
    margin: 0;
    text-shadow:
      -1px -1px 0 var(--ink-edge),
      1px -1px 0 var(--ink-edge),
      -1px 1px 0 var(--ink-edge),
      1px 1px 0 var(--ink-edge),
      2px 2px 3px rgba(90, 20, 50, 0.35);
  }
  .headline {
    top: 165px;
    font-family: "Courier Prime", "Courier New", monospace;
    font-size: 132px;
    font-weight: 400;
    line-height: 134px;
    letter-spacing: 2px;
  }
  .headline__line {
    display: block;
  }
  .headline__line--indent {
    padding-left: 20px;
  }
  .keyword {
    top: 700px;
    font-family: "Kalam", cursive;
    font-size: 262px;
    font-weight: 400;
    line-height: 1;
    letter-spacing: 0;
  }
</style>
</head>
<body>
  <main class="poster">
    <div class="poster__paint" role="img" aria-label="Painted pink, magenta and red acrylic texture background"></div>
    <svg class="poster__grain" viewBox="0 0 848 1200" aria-hidden="true">
      <filter id="canvas-grain">
        <feTurbulence type="fractalNoise" baseFrequency="0.012 0.05" numOctaves="4" seed="7"/>
        <feColorMatrix type="saturate" values="0"/>
      </filter>
      <rect width="848" height="1200" filter="url(#canvas-grain)"/>
    </svg>
    <h1 class="poster__text headline">
      <span class="headline__line">Do More</span>
      <span class="headline__line headline__line--indent">Of What</span>
      <span class="headline__line">Makes</span>
      <span class="headline__line">YOU</span>
    </h1>
    <p class="poster__text keyword">Happy</p>
  </main>
</body>
</html>
```